Medical VIP club - small design

Please read the specs in a design brief attached. Also we don't have logo in a Vector format and attaching the only version we have.

Industry/Entity Type

Club

```html
<!DOCTYPE html>
<html lang="en">
<head>
<meta charset="utf-8">
<title>Veloria — V.I.P Club</title>
<link href="https://fonts.googleapis.com/css2?family=Gelasio:ital,wght@0,400;0,600;0,700;1,400;1,600;1,700&display=swap" rel="stylesheet">
<style>
  :root {
    --bg-rust: #7c2d11;
    --bg-rust-dark: #5a1c0b;
    --bar-dark: #2d2410;
    --bar-dark-2: #3d3015;
    --footer-red: #4a0d0b;
    --footer-red-2: #3a0707;
    --panel: #e4cf98;
    --panel-light: #ead8a6;
    --panel-edge: #b99f66;
    --ink: #3b2c10;
    --ink-soft: #4d3c1a;
    --gold: #e8cf94;
    --gold-soft: #b7a06e;
    --dot: #c9b58a;
    --dot-active: #8a7a58;
    --cream: #f5e6c2;
  }
  * { margin: 0; padding: 0; box-sizing: border-box; }
  html, body { width: 1200px; height: 1096px; overflow: hidden; }
  body {
    font-family: "Gelasio", Georgia, serif;
    background: var(--bg-rust);
  }
  .page {
    position: relative;
    width: 1200px;
    height: 1096px;
    overflow: hidden;
    background: radial-gradient(ellipse 60% 55% at 50% 45%, #8a3614 0%, var(--bg-rust) 55%, var(--bg-rust-dark) 100%);
  }
  .top-bar {
    position: absolute; left: 0; top: 0; width: 1200px; height: 52px;
    background: linear-gradient(var(--bar-dark-2), var(--bar-dark));
  }
  .top-bar .registration {
    position: absolute; left: 873px; top: 22px;
    font-style: italic; font-weight: 700; font-size: 17px; color: var(--gold);
  }
  .top-bar .sign-in {
    position: absolute; left: 998px; top: 21px;
    font-style: italic; font-size: 16px; color: var(--gold); text-decoration: underline;
  }
  .brand {
    position: absolute; left: 112px; top: 78px;
    display: flex; align-items: center; gap: 8px;
    font-size: 46px; font-weight: 600; color: var(--gold-soft); line-height: 1;
  }
  .brand .mark { width: 14px; height: 14px; border-radius: 50%; background: var(--gold-soft); }
  .contact {
    position: absolute; left: 937px; top: 92px; height: 54px;
    border-left: 2px solid var(--gold-soft); padding-left: 14px;
    color: var(--cream);
  }
  .contact .label { font-weight: 700; font-size: 20px; line-height: 24px; }
  .contact .phone { font-size: 19px; line-height: 22px; }
  .panel {
    position: absolute; left: 112px; top: 170px; width: 967px; height: 818px;
    background: linear-gradient(var(--panel-light), var(--panel) 60%, #dcc48a);
    border: 1px solid var(--panel-edge);
    box-shadow: 0 2px 6px rgba(0,0,0,0.4);
  }
  .nav {
    position: absolute; left: 0; top: 3px; width: 965px; height: 33px;
    border-bottom: 3px solid #a58c5a;
    display: flex; align-items: center;
    font-size: 16px; color: var(--ink);
  }
  .nav a { color: inherit; text-decoration: none; text-align: center; }
  .nav .sep { width: 1px; height: 16px; background: var(--ink); }
  .nav .strong { font-weight: 700; font-size: 17px; }
  .hero {
    position: absolute; left: 10px; top: 57px; width: 945px; height: 351px;
    border: 2px solid #3b2a10;
    background: linear-gradient(90deg, #c9a25a 0%, #e7d7a8 25%, #f2ece0 50%, #e7d7a8 75%, #c9a25a 100%);
  }
  .hero-dots {
    position: absolute; left: 0; top: 420px; width: 965px;
    display: flex; justify-content: center; align-items: center; gap: 6px;
  }
  .hero-dots span {
    width: 20px; height: 20px; border: 1px solid #9a8a66; background: var(--dot); border-radius: 2px;
  }
  .hero-dots .active { width: 27px; height: 27px; background: var(--dot-active); }
  .divider {
    position: absolute; left: 10px; top: 451px; width: 945px;
    border-top: 1px dotted #5a4a28;
  }
  .section-label {
    position: absolute; left: 30px; top: 548px;
    font-style: italic; font-weight: 700; font-size: 20px; color: var(--ink);
  }
  .section-rule {
    position: absolute; left: 154px; top: 521px; width: 1px; height: 138px; background: var(--ink);
  }
  .club-title {
    position: absolute; left: 195px; top: 470px;
    font-style: italic; font-weight: 700; font-size: 18px; font-variant: small-caps;
    color: var(--ink); letter-spacing: 0.5px;
  }
  .club-copy {
    position: absolute; left: 195px; top: 516px; width: 730px;
    font-style: italic; font-size: 13.5px; line-height: 17px; color: var(--ink-soft);
  }
  .club-copy p + p { margin-top: 17px; }
  .follow {
    position: absolute; left: 771px; top: 785px;
    font-size: 14.5px; color: var(--ink);
  }
  .social {
    position: absolute; left: 862px; top: 776px; display: flex; gap: 4px;
  }
  .social span {
    width: 26px; height: 26px; border-radius: 3px;
    background: linear-gradient(#9d8d6a, #6f6248);
  }
  .footer {
    position: absolute; left: 0; top: 988px; width: 1188px; height: 108px;
    background: linear-gradient(var(--footer-red), var(--footer-red-2));
  }
  .footer-links {
    position: absolute; left: 122px; top: 46px;
    font-size: 14.5px; color: var(--gold-soft);
  }
  .footer-links .strong { font-weight: 700; }
  .copyright {
    position: absolute; left: 678px; top: 46px;
    font-size: 14.5px; color: var(--gold-soft);
  }
  .footer .brand { left: 955px; top: 25px; font-size: 32px; }
  .footer .brand .mark { width: 10px; height: 10px; }
</style>
</head>
<body>
<div class="page">
  <header class="top-bar">
    <span class="registration">Registration</span>
    <span class="sign-in">Sign In</span>
  </header>

  <div class="brand"><span class="mark"></span>Veloria</div>

  <div class="contact">
    <div class="label">Contact Us</div>
    <div class="phone">01480-552-317</div>
  </div>

  <main class="panel">
    <nav class="nav">
      <a style="width:100px">Home</a><span class="sep"></span>
      <a class="strong" style="width:140px">About Us</a><span class="sep"></span>
      <a style="width:140px">V.I.P Club</a><span class="sep"></span>
      <a style="width:153px">Services</a><span class="sep"></span>
      <a style="width:238px">Packages and Prices</a><span class="sep"></span>
      <a class="strong" style="width:176px">Registration</a>
    </nav>

    <div class="hero" role="img" aria-label="Photo of an elegant hotel lobby with marble floor, columns and a revolving entrance door"></div>

    <div class="hero-dots">
      <span></span><span></span><span class="active"></span><span></span><span></span><span></span><span></span><span></span>
    </div>

    <div class="divider"></div>

    <div class="section-label">About Us</div>
    <div class="section-rule"></div>

    <h2 class="club-title">Veloria V.I.P Club</h2>
    <div class="club-copy">
      <p>Background design is needed for a medical company that offers a membership in an Israeli medical center. The membership allows people to receive priority treatment (booking of best hotels, free consultations throughout the year and priority appointment for top Israeli doctors). Therefore target market are affluent Russian people.<br>Client seems to like this particular scheme, so all we need is to pretty it up and to create more concepts with different colors.</p>
      <p>Background design is needed for a medical company that offers a membership in an Israeli medical center. The membership allows people to receive priority treatment (booking of best hotels, free consultations throughout the year and priority appointment for top Israeli doctors). Therefore target market are affluent Russian people. Client seems to like this particular scheme, so all we need is to pretty it up and to create more concepts with different colors.</p>
    </div>

    <div class="follow">Follow us</div>
    <div class="social"><span></span><span></span><span></span></div>
  </main>

  <footer class="footer">
    <div class="footer-links">Home | Vip Club | Services &nbsp;| &nbsp;Packages and Prices &nbsp;| <span class="strong">Registration</span></div>
    <div class="copyright">© All Rights Reserved 2011 Veloria</div>
    <div class="brand"><span class="mark"></span>Veloria</div>
  </footer>
</div>
</body>
</html>
```